Records Management Company Revamp

We are looking to revamp our web presence, and need a catchy design that helps us to get noticed! We would like the website to be in wordpress. the main requirements are a home page, a landing page template for SEO / PPC, and then a few other pages that can be reused throughout the website.

We are happy to supply content / video etc.

Number of Pages Required

3 page

Font styles to use
Other font styles liked:
• Find fonts listed in attached branding document

Requirements
Must have
• Home page as well as sub pages according to their colours. Need to use colours and fonts set out in branding guide. Attached are examples of home page and sub pages.
Nice to have
• We have uploaded some very basic ideas we have of how we wish the website to look, but looking to have it more professional and fit together. Please see uploaded items.

```html
<!DOCTYPE html>
<html lang="en">
<head>
<meta charset="utf-8">
<title>Keepwell Storage – Home</title>
<link href="https://fonts.googleapis.com/css2?family=Bebas+Neue&family=Roboto:wght@400;500;700&display=swap" rel="stylesheet">
<style>
:root{
  --stage:#a9c9e2;
  --blue:#2a80c2;
  --blue-deep:#1d5f9a;
  --blue-bar:#174f82;
  --red:#d62637;
  --ink:#1f1f24;
  --muted:#7a7d85;
  --line:#e1e3e8;
  --band:#e8edf5;
  --white:#ffffff;
}
*{margin:0;padding:0;box-sizing:border-box}
html,body{width:1200px;height:1200px;overflow:hidden}
body{background:var(--stage);font-family:"Roboto",Arial,sans-serif;color:var(--ink);position:relative}
.page{position:absolute;background:var(--white);overflow:hidden;box-shadow:0 4px 18px rgba(20,50,80,.18)}
.page--home{left:58px;top:38px;width:581px;height:1162px;z-index:2}
.page--inner{left:559px;top:0;width:581px;height:1200px;z-index:1}
.abs{position:absolute}
.h-display{font-family:"Bebas Neue",Impact,sans-serif;font-weight:400;letter-spacing:.2px;line-height:1;color:var(--ink)}
.copy{font-size:4.6px;line-height:7.8px;color:var(--muted)}
.btn{position:absolute;background:var(--red);color:#fff;font-size:4.6px;font-weight:700;letter-spacing:.3px;display:flex;align-items:center;justify-content:center;text-transform:uppercase}

/* header */
.site-header{left:0;top:0;width:581px;height:32px;background:#fff}
.brand{left:0;top:0;width:101px;height:40px;background:var(--blue);z-index:3;display:flex;align-items:center;justify-content:center;gap:4px;color:#fff;font-size:9px;font-weight:700;letter-spacing:.3px}
.brand i{display:block;width:6px;height:6px;background:#fff}
.nav{right:48px;top:13px;display:flex;gap:13px;font-size:4.8px;font-weight:500;color:var(--ink)}
.cart{right:34px;top:11px}

/* hero */
.hero{left:0;top:32px;width:581px;height:238px;background:linear-gradient(100deg,#8c7a66 0%,#5d6473 35%,#3a4a60 60%,#6c7e96 100%)}
.hero-title{left:101px;top:112px;font-size:23px;color:#fff}
.hero-sub{left:101px;top:132px;font-size:9.5px;font-weight:700;color:#fff}
.hero-copy{left:101px;top:146px;width:180px;color:#e6e8ee}
.form-card{left:408px;top:62px;width:138px;height:179px;background:#fff;box-shadow:3px -2px 0 var(--blue)}
.form-card h3{position:absolute;left:16px;top:23px;font-size:11px;line-height:11px}
.field{position:absolute;left:16px;width:106px;border-bottom:1px solid var(--line);height:16px}
.field b{display:block;font-size:4.2px;font-weight:500;color:var(--ink)}
.field span{display:block;font-size:3.8px;color:#b9bcc3;margin-top:6px}

/* services */
.sec-title{font-size:19px}
.card{position:absolute;width:184px;height:140px;background:#fff;box-shadow:0 2px 6px rgba(0,0,0,.12)}
.card .img{position:absolute;left:0;top:0;width:184px;height:104px}
.card .cap{position:absolute;left:0;top:104px;width:184px;height:36px;display:flex;align-items:center;justify-content:space-between;padding:0 12px;font-size:9.5px;font-weight:500}
.card--active .cap{background:var(--red);color:#fff}

/* how it works */
.how{left:0;top:716px;width:581px;height:241px;background:linear-gradient(90deg,var(--blue) 0%,#2f7fbf 55%,#5b91c0 100%)}
.how ul{position:absolute;left:101px;top:67px;list-style:none}
.how li{display:flex;align-items:center;gap:6px;height:11.6px;font-size:4.6px;font-weight:700;color:#fff}
.how li i{display:block;width:6px;height:4px;border:1px solid #fff;border-radius:3px;position:relative}
.how li i::after{content:"";position:absolute;left:4px;top:1px;width:6px;height:1px;background:#fff}

.photo{position:absolute}

/* inner page */
.topband{left:0;top:0;width:581px;height:19px;background:var(--blue)}
.video{left:310px;top:290px;width:176px;height:144px;background:linear-gradient(135deg,#8e8a82,#4d5560 60%,#2e3640);box-shadow:3px -3px 0 var(--blue)}
.play{left:80px;top:63px;width:17px;height:17px;border-radius:50%;background:rgba(255,255,255,.35)}
.partners{left:0;top:470px;width:581px;height:99px;background:var(--band)}
.partner{position:absolute;top:46px;height:9px;border-radius:2px;background:#c8ceda}
.arrow-btn{position:absolute;width:21px;height:16px;background:var(--red);display:flex;align-items:center;justify-content:center}
.quote{left:150px;top:652px;width:283px;text-align:center;font-size:8.6px;line-height:12.8px;color:#3a3d45}
.map{left:107px;top:858px;width:190px;height:140px;background:linear-gradient(135deg,#cfe3ef,#e8e4d4 45%,#7fb0d6 70%,#d9e6c8);box-shadow:3px -3px 0 var(--blue)}
.area{position:absolute;left:324px;width:160px}
.area b{display:block;font-size:5px;font-weight:500;color:var(--ink)}
.area p{font-size:3.8px;line-height:7.5px;color:var(--muted);margin-top:2px}
.area-box{left:313px;top:892px;width:170px;height:35px;border:1px solid var(--red)}
.footer{left:0;top:1052px;width:581px;height:126px;background:var(--blue-deep);color:#fff}
.fcol{position:absolute;top:26px;font-size:4.8px;line-height:13px}
.fcol h4{font-size:5.8px;font-weight:700;line-height:8px;margin-bottom:4px}
.fcol u{text-decoration:underline}
.fbar{left:0;top:1178px;width:581px;height:22px;background:var(--blue-bar);color:#b9cde0;font-size:4px}
</style>
</head>
<body>

<!-- ============ INNER PAGE ============ -->
<section class="page page--inner">
  <div class="abs topband"></div>

  <h2 class="abs h-display sec-title" style="left:101px;top:54px">Meet Our Team</h2>
  <p class="abs copy" style="left:101px;top:78px;width:252px">Our friendly team handles every box, file and barcode with care. From first call to final delivery we stay close, answer fast and keep your records safe, sorted and always within easy reach.</p>

  <div class="photo" role="img" aria-label="Team member portrait" style="left:80px;top:122px;width:34px;height:120px;background:linear-gradient(#bfc4ca,#8b949c)"></div>
  <div class="photo" role="img" aria-label="Team member portrait" style="left:114px;top:134px;width:119px;height:121px;background:linear-gradient(#6c8fa8,#3e6c96)"></div>
  <div class="photo" role="img" aria-label="Team member portrait" style="left:233px;top:122px;width:120px;height:120px;background:linear-gradient(#d9b9a2,#c03c3c)"></div>
  <div class="photo" role="img" aria-label="Team member portrait" style="left:353px;top:134px;width:120px;height:121px;background:linear-gradient(#cdbb9e,#3d4a63)"></div>
  <div class="photo" role="img" aria-label="Team member portrait" style="left:473px;top:122px;width:108px;height:120px;background:linear-gradient(#c9c9c7,#5a5c60)"></div>

  <h2 class="abs h-display sec-title" style="left:101px;top:308px">Why Choose Us</h2>
  <p class="abs copy" style="left:101px;top:333px;width:182px">We have stored records for local firms for many years. Our site is secure, our staff are vetted and our drivers work to a tight schedule. You always know where each box is, who touched it and when it will arrive back on your desk.</p>
  <p class="abs copy" style="left:101px;top:380px;width:182px">Clear prices, no hidden fees and a fast reply to every request. We scan, store, shred and deliver so your team can get back to real work.</p>
  <div class="abs video" role="img" aria-label="Video still of a warehouse handshake">
    <div class="abs play"></div>
    <svg class="abs" style="left:86px;top:68px" width="7" height="8" viewBox="0 0 7 8"><path d="M0 0L7 4L0 8Z" fill="#fff"/></svg>
  </div>

  <div class="abs partners">
    <div class="partner" style="left:127px;width:50px"></div>
    <div class="partner" style="left:220px;width:30px"></div>
    <div class="partner" style="left:296px;width:32px"></div>
    <div class="partner" style="left:366px;width:44px"></div>
    <div class="partner" style="left:444px;width:52px"></div>
  </div>

  <h2 class="abs h-display sec-title" style="left:0;width:581px;text-align:center;top:602px">Testimonials</h2>
  <p class="abs" style="left:0;width:581px;text-align:center;top:628px;font-size:5.6px;color:#555">Our Happy Clients</p>
  <div class="arrow-btn" style="left:97px;top:668px"><svg width="10" height="6" viewBox="0 0 10 6"><path d="M10 3H1M3.5 .5L1 3l2.5 2.5" stroke="#fff" stroke-width=".9" fill="none"/></svg></div>
  <div class="arrow-btn" style="left:462px;top:668px"><svg width="10" height="6" viewBox="0 0 10 6"><path d="M0 3h9M6.5 .5L9 3 6.5 5.5" stroke="#fff" stroke-width=".9" fill="none"/></svg></div>
  <p class="abs quote">“Lorem ipsum dolor sit amet, consetetur sadipscing elitr, sed diam nonumy eirmod tempor invidunt ut labore et dolore magna aliquyam erat, sed diam voluptua. At vero eos et accusam et justo duo dolores et ea rebum.</p>
  <div class="abs" role="img" aria-label="Client portrait" style="left:280px;top:716px;width:22px;height:22px;border-radius:50%;background:linear-gradient(#c9a890,#6b5a4e)"></div>
  <p class="abs" style="left:0;width:581px;text-align:center;top:747px;font-size:5.4px;font-weight:700">Daniel Hart</p>
  <p class="abs" style="left:0;width:581px;text-align:center;top:757px;font-size:4.4px;color:var(--muted)">Chief Marketing Officer</p>

  <h2 class="abs h-display sec-title" style="left:101px;top:795px">Areas We Service</h2>
  <p class="abs copy" style="left:101px;top:819px;width:190px">We collect and deliver across the whole region every working day. Same day pickup is open for most postcodes near our main site.</p>
  <div class="abs map" role="img" aria-label="City map of the service region"></div>
  <div class="abs area-box"></div>
  <div class="area" style="top:862px"><b>Service Area 01</b><p>Daily pickups and returns for offices in the city centre and the nearby business parks.</p></div>
  <div class="area" style="top:898px"><b style="color:var(--red)">Service Area 01</b><p>Daily pickups and returns for offices in the city centre and the nearby business parks.</p></div>
  <div class="area" style="top:934px"><b>Service Area 01</b><p>Daily pickups and returns for offices in the city centre and the nearby business parks.</p></div>
  <div class="area" style="top:970px"><b>Service Area 01</b><p>Daily pickups and returns for offices in the city centre and the nearby business parks.</p></div>

  <footer class="abs footer">
    <div class="fcol" style="left:97px"><h4>OUR LINKS</h4>Offsitestorage<br>Document Shredding<br>Digitisation<br>Archive Supplies<br>Contact Us</div>
    <div class="fcol" style="left:203px;line-height:8.5px"><h4>LOCATION 1</h4>Larkstraat 12<br>3300 Velden<br><br>E&nbsp; <u>info@keepwellstorage.com</u><br>T&nbsp; 015550142<br><br>Company number:<br>BE 0000.123.456</div>
    <div class="fcol" style="left:309px;line-height:8.5px"><h4>LOCATION 2</h4>Larkstraat 12<br>3300 Velden<br><br>E&nbsp; <u>info@keepwellstorage.com</u><br>T&nbsp; 015550142<br><br>Company number:<br>BE 0000.123.456</div>
    <div class="fcol" style="left:427px"><h4>SOCIAL</h4>Friendlink<br>Chirper<br>Workgrid<br>Circles</div>
  </footer>
  <div class="abs fbar"><span class="abs" style="left:97px;top:9px">© 2018 KEEPWELL STORAGE</span><span class="abs" style="left:444px;top:9px">Privacy &nbsp;|&nbsp; Terms</span></div>
</section>

<!-- ============ HOME PAGE ============ -->
<section class="page page--home">
  <header class="abs site-header">
    <nav class="abs nav"><span>Home</span><span>Offsitestorage</span><span>Document Shredding</span><span>Digitisation</span><span>Archive Supplies</span><span>Contact Us</span></nav>
    <svg class="abs cart" width="10" height="9" viewBox="0 0 10 9"><path d="M0 1h2l1.3 5h5L9.5 2.5H2.6" stroke="#1f1f24" stroke-width=".8" fill="none"/><circle cx="4" cy="7.8" r=".8" fill="#1f1f24"/><circle cx="7.6" cy="7.8" r=".8" fill="#1f1f24"/><circle cx="8.5" cy="1.2" r="1.3" fill="#d62637"/></svg>
  </header>
  <div class="abs brand"><i></i>Keepwell Storage</div>

  <div class="abs hero" role="img" aria-label="Warehouse worker checking a tablet beside storage boxes"></div>
  <h1 class="abs h-display hero-title">Too Much Stuff?</h1>
  <p class="abs hero-sub">Not Enough Space? We Can Help!</p>
  <p class="abs copy hero-copy">We store, scan and shred your files so your office stays clear. Secure space, fast returns and fair prices for every business.</p>
  <div class="btn" style="left:101px;top:177px;width:70px;height:17px">Get Started!</div>

  <div class="abs form-card">
    <h3 class="h-display">Receive any of your<br>suggestions via email</h3>
    <div class="field" style="top:56px"><b>Full Name</b><span>John Doe</span></div>
    <div class="field" style="top:84px"><b>Email</b><span>johndoe@mail.com</span></div>
    <div class="field" style="top:113px"><b>Your Message</b><span>Hello</span></div>
    <div class="btn" style="left:16px;top:145px;width:106px;height:17px">Send Message</div>
  </div>

  <h2 class="abs h-display sec-title" style="left:101px;top:304px">Our Services</h2>
  <p class="abs copy" style="left:101px;top:328px;width:180px">We offer safe offsite storage, on site shredding, digital scans and boxes for your archive. Pick one service or bundle them all together.</p>
  <p class="abs copy" style="left:302px;top:328px;width:180px">Every job is tracked from pickup to return. Our team is here to help you choose the plan that fits your records and budget.</p>

  <div class="card" style="left:102px;top:369px"><div class="img" role="img" aria-label="Stacks of paper files on a desk" style="background:linear-gradient(#a88a6e,#d8d4d6 60%,#bfb9bd)"></div><div class="cap">Offsite Storage<svg width="11" height="7" viewBox="0 0 11 7"><path d="M0 3.5h10M7 .5l3 3-3 3" stroke="#d62637" stroke-width=".9" fill="none"/></svg></div></div>
  <div class="card" style="left:295px;top:382px"><div class="img" role="img" aria-label="Heap of shredded paper" style="background:linear-gradient(#54708d,#b9bfcc 55%,#e2e3e8)"></div><div class="cap">Document Shredding<svg width="11" height="7" viewBox="0 0 11 7"><path d="M0 3.5h10M7 .5l3 3-3 3" stroke="#d62637" stroke-width=".9" fill="none"/></svg></div></div>
  <div class="card card--active" style="left:102px;top:522px"><div class="img" role="img" aria-label="Open filing cabinet drawers" style="background:linear-gradient(#6f7884,#9aa1ab 55%,#c4b46a)"></div><div class="cap">Digitisation<svg width="11" height="7" viewBox="0 0 11 7"><path d="M0 3.5h10M7 .5l3 3-3 3" stroke="#fff" stroke-width=".9" fill="none"/></svg></div></div>
  <div class="card" style="left:295px;top:534px"><div class="img" role="img" aria-label="Shelves of archive boxes" style="background:linear-gradient(90deg,#c9ab86,#a98a66 60%,#9c2b3a)"></div><div class="cap">Archive Supplies<svg width="11" height="7" viewBox="0 0 11 7"><path d="M0 3.5h10M7 .5l3 3-3 3" stroke="#d62637" stroke-width=".9" fill="none"/></svg></div></div>

  <section class="abs how" aria-label="How offsite storage works">
    <h2 class="abs h-display sec-title" style="left:101px;top:30px;color:#fff">How Offsite Storage Works</h2>
    <ul>
      <li><i></i>We deliver boxes and Barcodes</li>
      <li><i></i>If you need them, we get you started with all the essentials to prepare your archives.</li>
      <li><i></i>We pick up your documents</li>
      <li><i></i>When your boxes are ready, let us know and we'll come by and collect your documents.</li>
      <li><i></i>WeStoreYourDocuments</li>
      <li><i></i>You documents are stored in our secure purpose-built facility in Eastvale.</li>
      <li><i></i>We Retrieve &amp; Deliver Your Documents</li>
      <li><i></i>When you need your documents, just call or email us and we'll get them to you!</li>
      <li><i></i>We Can Securely Destroy</li>
      <li><i></i>We can work with you ondetermining which documents can be securely destroyed and do this for you!</li>
    </ul>
    <div class="btn" style="left:101px;top:191px;width:70px;height:17px">Get Started!</div>
  </section>

  <h2 class="abs h-display sec-title" style="left:101px;top:990px">Meet Our Team</h2>
  <p class="abs copy" style="left:101px;top:1014px;width:252px">Our friendly team handles every box, file and barcode with care. From first call to final delivery we stay close, answer fast and keep your records safe, sorted and always within easy reach.</p>

  <div class="photo" role="img" aria-label="Team member portrait" style="left:0;top:1059px;width:114px;height:103px;background:linear-gradient(#a89f95,#3f3a36)"></div>
  <div class="photo" role="img" aria-label="Team member portrait" style="left:114px;top:1072px;width:120px;height:90px;background:linear-gradient(#6c8fa8,#3e6c96)"></div>
  <div class="photo" role="img" aria-label="Team member portrait" style="left:234px;top:1059px;width:120px;height:103px;background:linear-gradient(#d9b9a2,#c03c3c)"></div>
  <div class="photo" role="img" aria-label="Team member portrait" style="left:354px;top:1072px;width:118px;height:90px;background:linear-gradient(#cdbb9e,#3d4a63)"></div>
  <div class="photo" role="img" aria-label="Team member portrait" style="left:472px;top:1059px;width:109px;height:103px;background:linear-gradient(#c9c9c7,#5a5c60)"></div>
</section>

</body>
</html>
```